Over The Ridge Mediaworks Business Card
Card design
Over The Ridge Mediaworks Business Card -
Creative Brief
Simple
Simon Ashby
Chief Creative Officer
no address
Simon.Ashby@OverTheRidgeMediaworks.example
OverTheRidgeMediaworks.example
I don't have the source files from my logo project yet but will be uploading soon. Meanwhile please go to: http://entries.markcraftstudio.example/contests/over-the-ridge-logo and refer to winning draft #73 (also draft #5) I would like the front of the card to have the red-background logo plus the web address only
The back of the card will have the black-background logo plus all the personal information in white lettering. I would also like to see a version with the white-background logo and black lettering

```html
<!DOCTYPE html>
<html lang="en">
<head>
<meta charset="utf-8">
<title>Over The Ridge Mediaworks Business Card</title>
<link href="https://fonts.googleapis.com/css2?family=Archivo:wght@400;700&display=swap" rel="stylesheet">
<style>
  :root {
    --backdrop: #e4e4e4;
    --card-red: #c1272d;
    --card-black: #0d0d0d;
    --ink-white: #ffffff;
    --ink-black: #111111;
    --ink-soft: #d9d9d9;
  }
  * { margin: 0; padding: 0; box-sizing: border-box; }
  html, body {
    width: 1200px;
    height: 850px;
    overflow: hidden;
    background: var(--backdrop);
    font-family: "Archivo", Arial, sans-serif;
  }
  .canvas {
    position: relative;
    width: 1200px;
    height: 850px;
  }
  .card {
    position: absolute;
    overflow: hidden;
  }
  .card-front {
    left: 91px;
    top: 115px;
    width: 576px;
    height: 341px;
    background: var(--card-red);
  }
  .card-back {
    left: 533px;
    top: 391px;
    width: 583px;
    height: 329px;
    background: var(--card-black);
    color: var(--ink-white);
  }
  .brand-name {
    font-weight: 700;
    text-transform: uppercase;
    letter-spacing: 1px;
    line-height: 1;
    white-space: nowrap;
  }
  .brand-dot {
    display: block;
    flex: none;
    border-radius: 50%;
  }
  .front-brand {
    position: absolute;
    left: 0;
    right: 0;
    top: 118px;
    display: flex;
    justify-content: center;
    align-items: center;
    gap: 14px;
  }
  .front-brand .brand-name {
    color: var(--ink-white);
    font-size: 34px;
  }
  .front-brand .brand-dot {
    width: 22px;
    height: 22px;
    background: var(--ink-black);
  }
  .front-web {
    position: absolute;
    left: 0;
    right: 0;
    top: 278px;
    text-align: center;
    color: var(--ink-white);
    font-size: 17px;
    white-space: nowrap;
  }
  .back-brand {
    position: absolute;
    left: 211px;
    top: 72px;
    display: flex;
    align-items: center;
    gap: 8px;
  }
  .back-brand .brand-name {
    color: var(--ink-white);
    font-size: 18px;
  }
  .back-brand .brand-dot {
    width: 14px;
    height: 14px;
    background: var(--card-red);
  }
  .contact {
    position: absolute;
    left: 211px;
    top: 199px;
    white-space: nowrap;
  }
  .contact-name {
    font-size: 17px;
    font-weight: 700;
    letter-spacing: 0.5px;
    text-transform: uppercase;
  }
  .contact-title {
    font-size: 14px;
    color: var(--ink-soft);
    margin-top: 2px;
  }
  .contact-lines {
    margin-top: 40px;
    font-size: 14px;
    line-height: 20px;
    color: var(--ink-soft);
  }
</style>
</head>
<body>
  <main class="canvas">
    <section class="card card-front" aria-label="Business card front">
      <div class="front-brand">
        <span class="brand-name">Over The Ridge</span>
        <span class="brand-dot"></span>
      </div>
      <p class="front-web">OverTheRidgeMediaworks.example</p>
    </section>

    <section class="card card-back" aria-label="Business card back">
      <div class="back-brand">
        <span class="brand-name">Over The Ridge Mediaworks</span>
        <span class="brand-dot"></span>
      </div>
      <div class="contact">
        <p class="contact-name">Simon Ashby</p>
        <p class="contact-title">Chief Creative Officer</p>
        <div class="contact-lines">
          <p class="contact-phone">310 555 0148</p>
          <p class="contact-email">Simon.Ashby@OverTheRidgeMediaworks.example</p>
        </div>
      </div>
    </section>
  </main>
</body>
</html>
```